Roll Up Design Velumo

We are a beauty company and we need stunning design for our general roll-up banner that we gonna place just next to the main gate of mall that we are located in. The most important for us is the quality, accuracy and the unity of poster. It has to be super elegant, engaging and beautiful. Has to match our service standards (high). Colors do not matter as long as the overall look is exciting.
Examples and our logo are attached
Updates
Reason: We need more designs (more creativity, more quality, colurs and proportions).
Target Market(s)
Middle class ladies, students, business women
Industry/Entity Type
It Company
Colors
Designer to choose colors to be used in the design.
Look and feel
Each slider illustrates characteristics of the customer's brand and the style your logo design should communicate.

```html
<!DOCTYPE html>
<html lang="az">
<head>
<meta charset="utf-8">
<title>Velumo Gözəllik — Roll-up</title>
<link rel="stylesheet" href="https://fonts.googleapis.com/css2?family=Cinzel:wght@700&family=Roboto+Condensed:wght@400;700&family=Montserrat:wght@500&display=swap">
<style>
  :root {
    --bg-light: #f1e6e3;
    --bg-mid: #dccac5;
    --bg-deep: #c2aaa3;
    --brand-brown: #5b4a44;
    --band-brown: #5e4c45;
    --letter-line: #f3e8e4;
    --accent-red: #c0676a;
    --white: #ffffff;
    --photo-dark: #3a302c;
    --photo-mid: #8a766c;
    --photo-light: #c3aea4;
  }
  html, body {
    margin: 0;
    padding: 0;
    width: 1200px;
    height: 2857px;
    overflow: hidden;
  }
  .banner {
    position: relative;
    width: 1200px;
    height: 2857px;
    overflow: hidden;
    background:
      radial-gradient(ellipse 55% 30% at 60% 28%, rgba(255,255,255,0.6), transparent 70%),
      linear-gradient(180deg, var(--bg-light) 0%, var(--bg-mid) 50%, var(--bg-deep) 100%);
    font-family: "Roboto Condensed", "Arial Narrow", sans-serif;
  }
  .brand {
    position: absolute;
    top: 62px;
    left: 0;
    width: 100%;
    text-align: center;
  }
  .brand-name {
    margin: 0;
    font-family: "Cinzel", Georgia, serif;
    font-weight: 700;
    font-size: 112px;
    line-height: 1;
    letter-spacing: 6px;
    color: var(--brand-brown);
  }
  .brand-rule {
    width: 520px;
    height: 2px;
    margin: 22px auto 22px;
    background: var(--accent-red);
    opacity: 0.8;
  }
  .brand-sub {
    margin: 0;
    font-family: "Montserrat", sans-serif;
    font-weight: 500;
    font-size: 38px;
    letter-spacing: 3px;
    color: var(--brand-brown);
  }
  .tagline-band {
    position: absolute;
    top: 352px;
    left: 0;
    width: 100%;
    height: 286px;
    background: var(--band-brown);
  }
  .tagline {
    position: absolute;
    top: 378px;
    left: 571px;
    margin: 0;
    font-weight: 700;
    font-size: 92px;
    line-height: 1.22;
    color: var(--white);
  }
  .portrait {
    position: absolute;
    top: 830px;
    left: 560px;
    width: 640px;
    height: 1872px;
    background:
      radial-gradient(ellipse 22% 10% at 48% 10%, var(--photo-light), transparent 80%),
      radial-gradient(ellipse 45% 14% at 55% 35%, var(--photo-dark), transparent 80%),
      radial-gradient(ellipse 55% 35% at 50% 70%, var(--photo-mid), transparent 80%);
    -webkit-mask-image: linear-gradient(180deg, transparent 0%, #000 12%, #000 90%, transparent 100%);
    mask-image: linear-gradient(180deg, transparent 0%, #000 12%, #000 90%, transparent 100%);
    opacity: 0.75;
  }
  .vertical-name {
    position: absolute;
    top: 0;
    left: 0;
    width: 1200px;
    height: 2857px;
  }
  .vertical-name text {
    font-family: "Cinzel", Georgia, serif;
    font-weight: 700;
    fill: var(--brand-brown);
    stroke: var(--letter-line);
    stroke-width: 5px;
    paint-order: stroke;
  }
  .website {
    position: absolute;
    top: 2540px;
    left: 0;
    width: 100%;
    margin: 0;
    text-align: center;
    font-weight: 700;
    font-size: 104px;
    line-height: 1.1;
    color: var(--white);
    text-shadow: 0 3px 8px rgba(0,0,0,0.45);
  }
  .contact-band {
    position: absolute;
    left: 0;
    bottom: 0;
    width: 100%;
    height: 155px;
    background: var(--band-brown);
    display: flex;
    align-items: center;
    justify-content: center;
  }
  .contact {
    margin: 0;
    font-weight: 400;
    font-size: 52px;
    color: var(--white);
  }
</style>
</head>
<body>
<main class="banner">
  <header class="brand">
    <h1 class="brand-name">VELUMO</h1>
    <div class="brand-rule"></div>
    <p class="brand-sub">GÖZƏLLİK</p>
  </header>

  <div class="tagline-band"></div>
  <p class="tagline">Gözellik her<br>yandadir...</p>

  <div class="portrait" role="img" aria-label="Photo of an elegant woman in a dark velvet top and flowing taupe skirt, seated"></div>

  <svg class="vertical-name" viewBox="0 0 1200 2857" aria-hidden="true">
    <text x="0" y="0" font-size="540" textLength="2330" lengthAdjust="spacingAndGlyphs"
          transform="translate(464 2667) rotate(-90)">VELUMO</text>
  </svg>

  <p class="website">www.velumogozellik.com</p>

  <footer class="contact-band">
    <p class="contact">office@velumogozellik.com | (012) 555 0148</p>
  </footer>
</main>
</body>
</html>
```